A Health & Fitness Website selling saunas and Cold tubs

www.brightkestrelhub.com, www.velmoraquarter, www.tindalewharfhouse
Design a website
We are selling saunas, infrared saunas, cold plunge tubs, and massage chairs to financially successful MEN.
We want professional, simple, masculine with a touch of sexy.
One section for each… saunas, cold plunge tubs, massage chairs.
Each will have at least two buy links to their affiliate/supplier/store.
The landing page / opening page / needs big & bold; a full screen image? a great picture showing the warmth of a sauna? Need your ideas
The pictures are everything.

The Website for our book
https://marigoldtrackwayclub.com/

• Great pictures

```html
<!DOCTYPE html>
<html lang="en">
<head>
<meta charset="utf-8">
<title>Marla Quinn Fitness — Saunas, Cold Plunge Tubs & Massage Chairs</title>
<link href="https://fonts.googleapis.com/css2?family=Roboto:wght@400;500;700&family=Quicksand:wght@400;500&family=Cormorant+Garamond:ital,wght@1,500&family=Montserrat:wght@400;500&display=swap" rel="stylesheet">
<style>
:root{
  --bronze:#b8782f;
  --bronze-dark:#a86c28;
  --bronze-soft:#e8dccf;
  --ink:#2b2b2b;
  --text:#444;
  --muted:#666;
  --light:#f4f4f4;
  --white:#fff;
  --footer:#b07a3a;
}
*{box-sizing:border-box;margin:0;padding:0}
html,body{width:1200px;height:3484px;overflow:hidden;background:var(--white)}
body{font-family:"Roboto",sans-serif;color:var(--text)}
.page{position:relative;width:1200px;height:3484px;overflow:hidden}
.abs{position:absolute}

/* hero */
.hero{left:0;top:0;width:1200px;height:625px;
  background:linear-gradient(100deg,#2a1a10 0%,#4a2c17 35%,#8a5630 60%,#b77a45 80%,#6b4024 100%)}
.brand{left:111px;top:54px;display:flex;align-items:center;gap:12px}
.brand-dot{width:22px;height:22px;border-radius:50%;background:var(--white)}
.brand-name{font-family:"Roboto",sans-serif;font-weight:700;font-size:22px;color:var(--white)}
.hero-title{left:111px;top:224px;font-weight:700;font-size:40px;line-height:51px;color:var(--white)}
.hero-sub{left:113px;top:338px;font-weight:500;font-size:17px;line-height:26px;color:var(--white)}

.pill{background:var(--white);border-radius:68px;box-shadow:0 10px 24px rgba(0,0,0,.14);
  text-align:center;color:var(--bronze);font-weight:500}
.pill-top{left:111px;top:583px;width:977px;height:135px;padding-top:24px;font-size:38px;line-height:46px}
.pill-top .second{font-size:35px}

/* benefits */
.benefits-title{left:111px;top:800px;width:800px;font-weight:700;font-size:35px;line-height:43px;color:var(--ink)}
.rule{height:3px;background:var(--bronze)}
.benefits-rule{left:111px;top:900px;width:261px}
.benefit-list{left:111px;top:976px;list-style:none}
.benefit-list li{display:flex;align-items:center;gap:8px;height:34.5px;font-size:17.5px;color:#333}
.benefit-list svg{width:22px;height:24px;flex:none}
.benefits-note{left:111px;top:1190px;font-weight:500;font-size:27px;color:var(--bronze)}
.ring{left:767px;top:885px;width:324px;height:324px;border-radius:50%;
  border:8px solid var(--bronze);border-left-color:transparent;border-top-color:var(--bronze)}
.round-photo{left:769px;top:901px;width:292px;height:292px;border-radius:50%;
  background:radial-gradient(circle at 50% 45%,#a7714a,#6e4527 70%,#4a2c16)}

/* product bands */
.band{left:0;width:1200px}
.band-warm{background:linear-gradient(120deg,#b57635 0%,#c48745 45%,#b97b3a 70%,#a96c2d 100%)}
.band-sauna{top:1303px;height:487px}
.band-cold{top:1790px;height:486px;background:var(--light)}
.band-massage{top:2276px;height:552px}
.photo{border-radius:40px 0 40px 40px;border-top-right-radius:0}
.photo-frame{border-radius:40px}
.photo-back{border-radius:40px}
.band-warm .photo-back{background:rgba(255,255,255,.22)}
.band-cold .photo-back{background:var(--bronze-soft)}
.sauna-photo{background:linear-gradient(135deg,#8a5a33,#c48e5a 55%,#6a4226)}
.cold-photo{background:linear-gradient(160deg,#cfd8dc,#9aa6ad 50%,#44505a)}
.massage-photo{background:linear-gradient(135deg,#7a8a4a 0%,#e7d6c4 35%,#b5835f 70%,#f1ece6)}

.prod-title{font-weight:700;font-size:35px}
.band-warm .prod-title{color:var(--white)}
.band-cold .prod-title{color:var(--bronze)}
.prod-copy{width:490px;font-size:15.5px;line-height:26.5px;text-align:justify}
.band-warm .prod-copy{color:var(--white)}
.band-cold .prod-copy{color:#555}
.btn{display:inline-flex;align-items:center;justify-content:center;width:133px;height:44px;
  border-radius:10px;font-weight:500;font-size:15.5px;margin-right:10px;box-shadow:0 3px 6px rgba(0,0,0,.12)}
.band-warm .btn{background:var(--white);color:var(--bronze)}
.band-cold .btn{background:var(--bronze);color:var(--white)}

.pill-bottom{left:111px;top:2760px;width:977px;height:137px;padding-top:42px;font-size:40px}

/* testimonials */
.testi-title{left:0;top:2978px;width:1200px;text-align:center;font-weight:700;font-size:35px;color:var(--ink)}
.testi-rule{left:499px;top:3028px;width:203px;height:2px}
.card{top:3083px;width:318px;height:218px;background:var(--white);border-radius:20px;
  box-shadow:0 4px 18px rgba(0,0,0,.1);padding:26px 26px 0;overflow:hidden}
.card-head{display:flex;justify-content:space-between;align-items:flex-start;height:60px}
.quote{width:50px;height:50px;border-radius:50%;border:2px solid #ccc;display:flex;align-items:center;justify-content:center;
  font-family:Georgia,serif;font-weight:700;font-size:46px;line-height:1;color:#c9c9c9;padding-top:18px}
.card.active .quote{border-color:#1f2a44;color:#1f2a44}
.who{text-align:center}
.who .name{font-family:"Cormorant Garamond",serif;font-style:italic;font-weight:500;font-size:21px;color:#333}
.who .stars{font-size:13px;color:var(--bronze);letter-spacing:1px}
.card p{font-family:"Quicksand",sans-serif;font-size:13.5px;line-height:24px;color:#555;text-align:justify;height:96px;overflow:hidden;margin-top:8px}
.dots{left:558px;top:3333px;display:flex;gap:6px}
.dots span{width:17px;height:17px;border-radius:50%;background:#bdbdbd}
.dots span:first-child{background:var(--bronze)}

.footer{left:0;top:3438px;width:1200px;height:46px;background:var(--footer);color:var(--white);
  font-family:"Montserrat",sans-serif;font-size:18.5px;text-align:center;line-height:46px}
</style>
</head>
<body>
<div class="page">

  <section class="abs hero" role="img" aria-label="Photo of a relaxed man and woman resting in a warm wooden sauna"></section>
  <div class="abs brand"><span class="brand-dot"></span><span class="brand-name">Marla Quinn Fitness</span></div>
  <h1 class="abs hero-title">Dramatically Improve Your Health<br>Without Exercise</h1>
  <p class="abs hero-sub">Successful Men Recognize the Importance of Their Health<br>and Make it a Priority.&nbsp; It’s Your Time.&nbsp; You’ve Earned it.</p>

  <div class="abs pill pill-top">A Mans Body Thrives on Circulation<br><span class="second">And It Doesn’t Care How You Get It.</span></div>

  <h2 class="abs benefits-title">When there’s no time for exercise. use Hot, Cold, or Massage. The Benefits are Numerous.</h2>
  <div class="abs rule benefits-rule"></div>
  <ul class="abs benefit-list">
    <li><svg viewBox="0 0 22 24"><path d="M2 2h18L11 13z M11 13v8 M5 22h12" fill="none" stroke="#b8782f" stroke-width="2.4" stroke-linejoin="round"/></svg>Relieve Stress&nbsp; -&nbsp; Detox Your Pores&nbsp; -&nbsp; Sleep Better</li>
    <li><svg viewBox="0 0 22 24"><path d="M2 2h18L11 13z M11 13v8 M5 22h12" fill="none" stroke="#b8782f" stroke-width="2.4" stroke-linejoin="round"/></svg>Relieve Muscle Tension&nbsp; -&nbsp; Boost Energy Levels</li>
    <li><svg viewBox="0 0 22 24"><path d="M2 2h18L11 13z M11 13v8 M5 22h12" fill="none" stroke="#b8782f" stroke-width="2.4" stroke-linejoin="round"/></svg>Increase Testosterone&nbsp; -&nbsp; Reduce Inflammation&nbsp; -&nbsp; Increase Immunity&nbsp; Reduce</li>
    <li><svg viewBox="0 0 22 24"><path d="M2 2h18L11 13z M11 13v8 M5 22h12" fill="none" stroke="#b8782f" stroke-width="2.4" stroke-linejoin="round"/></svg>Depression&nbsp; -&nbsp;&nbsp; Alleviate Joint Pain&nbsp; -&nbsp; Healthier Skin</li>
    <li><svg viewBox="0 0 22 24"><path d="M2 2h18L11 13z M11 13v8 M5 22h12" fill="none" stroke="#b8782f" stroke-width="2.4" stroke-linejoin="round"/></svg>Lower the Risk of Cardiovascular Disease&nbsp; -&nbsp; Increase Metabolism</li>
    <li><svg viewBox="0 0 22 24"><path d="M2 2h18L11 13z M11 13v8 M5 22h12" fill="none" stroke="#b8782f" stroke-width="2.4" stroke-linejoin="round"/></svg>Promote Weight Loss&nbsp; -&nbsp; A Longer &amp; Healthier Life</li>
  </ul>
  <p class="abs benefits-note">Specific Improvements will be Individual to You.</p>
  <div class="abs ring"></div>
  <div class="abs round-photo" role="img" aria-label="Photo of a man relaxing on a sauna bench with a towel"></div>

  <!-- Saunas -->
  <section class="abs band band-warm band-sauna" role="img" aria-label="Warm tinted background photo of a woman in a sauna">
    <div class="abs photo-back" style="left:183px;top:118px;width:361px;height:281px"></div>
    <div class="abs photo-frame sauna-photo" style="left:111px;top:87px;width:398px;height:288px" role="img" aria-label="Photo of a man sitting in a wooden sauna"></div>
    <h3 class="abs prod-title" style="left:600px;top:78px">Saunas</h3>
    <p class="abs prod-copy" style="left:601px;top:132px">Lorem ipsum dolor sit amet, consectetur adipiscing elit, sed do eiusmod tempor incididunt ut labore et dolore magna aliqua. Quis ipsum suspendisse ultrices gravida. Risus commodo viverra maecenas accumsan lacus vel facilisis.</p>
    <div class="abs" style="left:601px;top:257px"><span class="btn">BUY NOW</span><span class="btn">CONTACT US</span></div>
  </section>

  <!-- Cold plunge -->
  <section class="abs band band-cold">
    <h3 class="abs prod-title" style="left:111px;top:80px">Cold Plunge Tubs</h3>
    <p class="abs prod-copy" style="left:111px;top:130px">Lorem ipsum dolor sit amet, consectetur adipiscing elit, sed do eiusmod tempor incididunt ut labore et dolore magna aliqua. Quis ipsum suspendisse ultrices gravida. Risus commodo viverra maecenas accumsan lacus vel facilisis.</p>
    <div class="abs" style="left:111px;top:257px"><span class="btn">BUY NOW</span><span class="btn">CONTACT US</span></div>
    <div class="abs photo-back" style="left:654px;top:114px;width:361px;height:284px"></div>
    <div class="abs photo-frame cold-photo" style="left:691px;top:87px;width:397px;height:285px" role="img" aria-label="Photo of a man splashing in an icy cold plunge"></div>
  </section>

  <!-- Massage chairs -->
  <section class="abs band band-warm band-massage" role="img" aria-label="Warm tinted background photo of a massage">
    <div class="abs photo-back" style="left:183px;top:112px;width:361px;height:284px"></div>
    <div class="abs photo-frame massage-photo" style="left:111px;top:85px;width:398px;height:286px" role="img" aria-label="Photo of a man receiving a back massage"></div>
    <h3 class="abs prod-title" style="left:598px;top:76px">Massage Chairs</h3>
    <p class="abs prod-copy" style="left:601px;top:130px">Lorem ipsum dolor sit amet, consectetur adipiscing elit, sed do eiusmod tempor incididunt ut labore et dolore magna aliqua. Quis ipsum suspendisse ultrices gravida. Risus commodo viverra maecenas accumsan lacus vel facilisis.</p>
    <div class="abs" style="left:601px;top:254px"><span class="btn">BUY NOW</span><span class="btn">CONTACT US</span></div>
  </section>

  <div class="abs pill pill-bottom">Everything Works Better with Increased Blood Flow</div>

  <!-- Testimonials -->
  <h2 class="abs testi-title">Our Testimonials</h2>
  <div class="abs rule testi-rule"></div>

  <article class="abs card" style="left:-253px">
    <div class="card-head"><span class="quote">“</span><div class="who"><div class="name">- Christopher</div><div class="stars">★★★★☆</div></div></div>
    <p>I have never felt better than I do with the plunge. I use it at least once a day. I</p>
  </article>
  <article class="abs card active" style="left:95px">
    <div class="card-head"><span class="quote">“</span><div class="who"><div class="name">- Alexander</div><div class="stars">★★★★☆</div></div></div>
    <p>I had no idea how much inflammation I had in my body. It wasn’t until the relief I got from my cold plunge that I realized how bad joints were. It’s been a life</p>
  </article>
  <article class="abs card" style="left:442px">
    <div class="card-head"><span class="quote">“</span><div class="who"><div class="name">- William</div><div class="stars">★★★★☆</div></div></div>
    <p>My massage chair has been a life saver. Having back pain for years the chair gives me the relief I need. I can dial in for a deep massage or gentle pressure. I would never</p>
  </article>
  <article class="abs card" style="left:789px">
    <div class="card-head"><span class="quote">“</span><div class="who"><div class="name">- Andrew</div><div class="stars">★★★★☆</div></div></div>
    <p>I pretty much spend my life at the office. There’s no way I’m going to get a cold tub or a sauna. I have the space at home for a massage chair and it’s heaven. I have</p>
  </article>
  <article class="abs card" style="left:1135px">
    <div class="card-head"><span class="quote">“</span><div class="who"><div class="name">- Thomas</div><div class="stars">★★★★☆</div></div></div>
    <p>I’d swear by my sauna. A couple of sessions and I found that it eases extreme tension.</p>
  </article>

  <div class="abs dots"><span></span><span></span><span></span><span></span></div>

  <footer class="abs footer">Copyright 2024 Marla Quinn Fitness&nbsp; |&nbsp; All Rights Reserved.</footer>
</div>
</body>
</html>
```